Business Card Design Project

We are an agricultural business based in Brisbane.
We design, manage and operate regional saleyards. Our logo is green/silver in colour and details of our business can be found on our website www.vodemarketyards.com.au

Just wanting a corporate design for some business cards and include name, position, contact details.

Thanks

Industry/Entity Type

Business

```html
<!DOCTYPE html>
<html lang="en">
<head>
<meta charset="utf-8">
<title>Vode Market Yards – Business Card</title>
<link rel="stylesheet" href="https://fonts.googleapis.com/css2?family=Roboto+Slab:wght@300;400;700&family=Arimo:wght@400&display=swap">
<style>
  :root {
    --backdrop: #f1ede6;
    --card-front: #d8d9da;
    --card-back: #fbfbfb;
    --ink: #222222;
    --ink-soft: #3a3a3a;
    --brand-green: #13873f;
    --icon: #333333;
    --edge: rgba(0,0,0,0.08);
  }
  * { margin: 0; padding: 0; box-sizing: border-box; }
  html, body { width: 1200px; height: 900px; overflow: hidden; background: var(--backdrop); }
  .canvas { position: relative; width: 1200px; height: 900px; }

  .card {
    position: absolute;
    width: 660px;
    height: 395px;
    border: 1px solid var(--edge);
  }
  .card--front { left: 62px; top: 63px; background: var(--card-front); display: flex; align-items: center; justify-content: center; }
  .card--back { left: 480px; top: 411px; background: var(--card-back); }

  .wordmark {
    font-family: "Roboto Slab", Georgia, serif;
    font-weight: 700;
    color: var(--ink);
    text-transform: uppercase;
    text-align: center;
    line-height: 1.05;
  }
  .wordmark--large { font-size: 48px; letter-spacing: 0.5px; }
  .wordmark--small {
    position: absolute; left: 58px; top: 64px;
    font-size: 18px; text-align: left;
    display: flex; align-items: center; gap: 10px;
  }
  .wordmark__square { width: 14px; height: 14px; background: var(--ink); flex: none; }

  .person {
    position: absolute; right: 60px; top: 168px; text-align: right;
    font-family: "Roboto Slab", Georgia, serif;
  }
  .person__name { font-size: 29px; font-weight: 300; color: var(--ink); line-height: 1.1; }
  .person__surname { color: var(--brand-green); font-weight: 400; }
  .person__role { font-size: 13px; font-weight: 400; color: var(--ink-soft); margin-top: 2px; letter-spacing: 0.3px; }

  .contacts {
    position: absolute; top: 261px;
    list-style: none;
    font-family: "Arimo", Arial, sans-serif;
    font-size: 14px; color: var(--ink-soft);
  }
  .contacts--left { left: 168px; }
  .contacts--right { left: 404px; }
  .contacts li { display: flex; align-items: center; height: 25px; }
  .contacts svg { width: 13px; height: 13px; margin-right: 8px; flex: none; fill: var(--icon); }
  .contacts .spacer { width: 21px; flex: none; }
</style>
</head>
<body>
<div class="canvas">

  <section class="card card--front">
    <div class="wordmark wordmark--large">Vode Market<br>Yards</div>
  </section>

  <section class="card card--back">
    <div class="wordmark wordmark--small">
      <span class="wordmark__square"></span>
      <span>Vode Market<br>Yards</span>
    </div>

    <div class="person">
      <div class="person__name">Daniel <span class="person__surname">Hartigan</span></div>
      <div class="person__role">General Manager</div>
    </div>

    <ul class="contacts contacts--left">
      <li>
        <svg viewBox="0 0 16 16"><path d="M8 0a5.5 5.5 0 0 0-5.5 5.5C2.5 9.6 8 16 8 16s5.5-6.4 5.5-10.5A5.5 5.5 0 0 0 8 0zm0 8a2.5 2.5 0 1 1 0-5 2.5 2.5 0 0 1 0 5z"/></svg>
        Your Street,
      </li>
      <li><span class="spacer"></span>City, Pincode</li>
      <li>
        <svg viewBox="0 0 16 16"><path d="M8 0a8 8 0 1 0 0 16A8 8 0 0 0 8 0zm0 1.5c.9 0 2 1.7 2.4 4.5H5.6C6 3.2 7.1 1.5 8 1.5zM1.6 7.5h2.6c0 .4 0 .7.1 1H1.6zm.3 2h2.5c.2 1.6.6 2.9 1.2 3.9A6.5 6.5 0 0 1 1.9 9.5zM4.2 6H1.9a6.5 6.5 0 0 1 3.7-3.4C5 3.6 4.5 4.7 4.2 6zm3.8 8.5c-.9 0-2-1.7-2.4-5h4.8c-.4 3.3-1.5 5-2.4 5zm2.4-5h2.5a6.5 6.5 0 0 1-3.7 3.9c.6-1 1-2.3 1.2-3.9zm.1-1c0-.3.1-.6.1-1h2.6c0 .4 0 .7-.1 1zm1.3-2.5c-.3-1.3-.8-2.4-1.4-3.4A6.5 6.5 0 0 1 14.1 6z"/></svg>
        www.vodemarketyards.com.au
      </li>
    </ul>

    <ul class="contacts contacts--right">
      <li>
        <svg viewBox="0 0 16 16"><path d="M4.5 1 7 4.5 5.5 6c.7 1.8 2.2 3.3 4 4L11 8.5l3.5 2.5-1.5 3C7 14 2 9 2 3z"/></svg>
        0400 318 672
      </li>
      <li>
        <svg viewBox="0 0 16 16"><path d="M4 1h6l2 2v3h2a1 1 0 0 1 1 1v5h-3v3H4v-3H1V7a1 1 0 0 1 1-1h2zm1 1v4h6V3.5L9.5 2zm0 8v4h6v-4z"/></svg>
        +(000) 5502 1180
      </li>
      <li>
        <svg viewBox="0 0 16 16"><path d="M1 3h14v10H1zm1.5 1.2v.3L8 8.6l5.5-4.1v-.3zm0 2.1v5.2h11V6.3L8 10.4z"/></svg>
        daniel@vodeyards.com.au
      </li>
    </ul>
  </section>

</div>
</body>
</html>
```